Yard Sign Design for Roofing Contractor

We are looking for a new design for our yard signs used on all jobs we build. We are looking for a way to brand the company and are hoping that this contest can give us a "theme" we can incorporate into out other marketing items such as, vehicle graphics, apparel, etc... I have attached a copy of our logo to be used on the sign, it can be "shadowed" with a color to enhance the look and the sign, but please keep the basic logo design. Attached are some samples of construction colors the boss was thinking of along with a picture of our current yard sign to help give some direction and let you know what info is needed on the sign.The darker construction yellow may work better than the fluorescent yellow, but won't know without visual aid. We are not tied to any particular color as of now, so they do have freedom of design as long as keeping with the construction feel. (Just another thought, potentially a reflective construction tape look would be interesting so signs are visable at night)
Updates

Reason: Meeting with new web designers next week to discuss best option to incorporate into our website.Thank you for the submissions!

Target Market(s)

Want signs to stand out when driving by and visibility in neighborhood where sign is posted for potential referrals

Industry/Entity Type

Contractor

Colors
fbed22
fece3e
f37122

Requirements
Must have
• Information that is on our current signs, image attached. I uploaded a .pdf file showing some options that could work for adding "shading" to our logo if you choose to do so.
• Sign should measure 18" T, 24" W
Nice to have
• Interested is seeing designs using construction tape look, images attached

```html
<!DOCTYPE html>
<html lang="en">
<head>
<meta charset="utf-8">
<title>Crestline Construction – Yard Sign</title>
<link rel="stylesheet" href="https://fonts.googleapis.com/css2?family=Cinzel:wght@700&family=Montserrat:wght@600;700&display=swap">
<style>
  :root {
    --backdrop: #e7e4df;
    --tape-yellow: #fece3e;
    --tape-yellow-deep: #f6bd22;
    --tape-black: #111111;
    --metal-light: #eeeeee;
    --metal-mid: #c9c9c9;
    --metal-dark: #a9a9a9;
    --frame-line: #5e5e5e;
    --ink: #0d0d0d;
    --screw-face: #8c8c8c;
  }
  * { box-sizing: border-box; margin: 0; padding: 0; }
  html, body {
    width: 1200px; height: 1200px; overflow: hidden;
    background: var(--backdrop);
  }
  .yard-sign {
    position: absolute; left: 40px; top: 180px;
    width: 1120px; height: 840px;
    background: repeating-linear-gradient(
      -45deg,
      var(--tape-yellow) 0 40px,
      var(--tape-black) 40px 62px
    );
    box-shadow: 0 10px 28px rgba(0,0,0,.25);
  }
  .yard-sign::before {
    content: ""; position: absolute; inset: 0;
    background: linear-gradient(90deg, rgba(246,189,34,.25), rgba(255,255,255,0) 40%, rgba(246,189,34,.3));
    pointer-events: none;
  }
  .metal-plate {
    position: absolute; left: 54px; top: 47px; right: 54px; bottom: 52px;
    background:
      repeating-linear-gradient(0deg, rgba(255,255,255,.12) 0 1px, rgba(0,0,0,.03) 1px 3px),
      linear-gradient(105deg, var(--metal-dark) 0%, var(--metal-light) 30%, var(--metal-mid) 55%, var(--metal-light) 78%, var(--metal-dark) 100%);
    box-shadow: 0 4px 10px rgba(0,0,0,.35);
  }
  .plate-frame {
    position: absolute; inset: 28px;
    border: 3px solid var(--frame-line);
    border-radius: 18px;
  }
  .screw {
    position: absolute; width: 30px; height: 30px;
  }
  .screw.tl { left: 40px; top: 40px; }
  .screw.tr { right: 40px; top: 40px; }
  .screw.bl { left: 40px; bottom: 40px; }
  .screw.br { right: 40px; bottom: 40px; }
  .sign-content {
    position: absolute; inset: 0;
    display: flex; flex-direction: column; align-items: center;
    color: var(--ink);
  }
  .company-name {
    margin-top: 150px;
    font-family: "Cinzel", serif; font-weight: 700;
    text-align: center; line-height: 1;
  }
  .company-name .name-main { display: block; font-size: 128px; letter-spacing: -1px; }
  .company-name .name-sub { display: block; font-size: 70px; margin-top: 14px; letter-spacing: -1px; }
  .services {
    margin-top: 64px;
    display: flex; gap: 88px;
    font-family: "Cinzel", serif; font-weight: 700;
    font-size: 36px; line-height: 1;
  }
  .phone {
    margin-top: 38px;
    display: flex; align-items: center; gap: 18px;
    font-family: "Montserrat", sans-serif; font-weight: 700;
    font-size: 74px; line-height: 1;
  }
  .phone-icon { width: 64px; height: 64px; }
  .website {
    margin-top: 22px;
    font-family: "Montserrat", sans-serif; font-weight: 600;
    font-size: 36px; letter-spacing: .34em; line-height: 1;
  }
</style>
</head>
<body>
  <div class="yard-sign">
    <div class="metal-plate">
      <div class="plate-frame"></div>
      <svg class="screw tl" viewBox="0 0 30 30" aria-hidden="true"><circle cx="15" cy="15" r="14" fill="var(--screw-face)"/><line x1="8" y1="22" x2="22" y2="8" stroke="#d8d8d8" stroke-width="3"/></svg>
      <svg class="screw tr" viewBox="0 0 30 30" aria-hidden="true"><circle cx="15" cy="15" r="14" fill="var(--screw-face)"/><line x1="8" y1="22" x2="22" y2="8" stroke="#d8d8d8" stroke-width="3"/></svg>
      <svg class="screw bl" viewBox="0 0 30 30" aria-hidden="true"><circle cx="15" cy="15" r="14" fill="var(--screw-face)"/><line x1="8" y1="22" x2="22" y2="8" stroke="#d8d8d8" stroke-width="3"/></svg>
      <svg class="screw br" viewBox="0 0 30 30" aria-hidden="true"><circle cx="15" cy="15" r="14" fill="var(--screw-face)"/><line x1="8" y1="22" x2="22" y2="8" stroke="#d8d8d8" stroke-width="3"/></svg>

      <div class="sign-content">
        <h1 class="company-name">
          <span class="name-main">CRESTLINE</span>
          <span class="name-sub">CONSTRUCTION</span>
        </h1>
        <div class="services">
          <span>Roof</span><span>Siding</span><span>Gutters</span>
        </div>
        <div class="phone">
          <svg class="phone-icon" viewBox="0 0 64 64" aria-hidden="true">
            <circle cx="32" cy="32" r="28" fill="none" stroke="var(--ink)" stroke-width="4"/>
            <path d="M22 17c3-2 6-1 7 2l3 7c1 2 0 4-2 5l-3 2c2 5 5 9 10 12l2-3c1-2 3-3 5-2l7 3c2 1 3 4 1 6l-3 3c-3 3-9 2-16-3-8-6-14-15-15-22 0-4 1-7 4-10z" fill="var(--ink)"/>
          </svg>
          <span>1-405-555-0142</span>
        </div>
        <div class="website">www.crestlineroofing.com</div>
      </div>
    </div>
  </div>
</body>
</html>
```